New Business Cards for MB&LR

We need updated business cards for a staff of 15 engineers, estimators, project managers, and sales people. We have recently begun changes to our website and marketing material to improve our look and branding. We are an established fabricator specializing in pressure vessels, tanks, and structural steel. The owners require us to use the existing logo and old english text design. Also, we prefer dark grey or mostly black cards.
Target Market(s)
Engineers, purchasing agents, estimators, and project managers of; mining companies, refineries, industrial construction professionals
Industry/Entity Type
Business
Contact Information for Business Card
Logo, phone, website, email, etc.
Look and feel

```html
<!DOCTYPE html>
<html lang="en">
<head>
<meta charset="utf-8">
<title>MB&amp;LR Business Card</title>
<link rel="stylesheet" href="https://fonts.googleapis.com/css2?family=Roboto+Condensed:wght@400;700&display=swap">
<style>
  :root {
    --stage: #d9d9d7;
    --card-black: #121212;
    --card-white: #f1f1ef;
    --silver-light: #e6e6e6;
    --silver-dark: #8a8a8a;
    --gold: #c99a2e;
    --maroon: #5a1a1e;
    --text-light: #e4e4e4;
    --text-dark: #1a1a1a;
  }
  * { box-sizing: border-box; margin: 0; padding: 0; }
  html, body { width: 1200px; height: 961px; overflow: hidden; }
  body {
    background: var(--stage);
    font-family: "Roboto Condensed", "Arial Narrow", sans-serif;
    position: relative;
  }
  .card {
    position: absolute;
    left: 250px;
    width: 700px;
    height: 400px;
    overflow: hidden;
    box-shadow: 0 6px 18px rgba(0,0,0,.25);
  }
  .card--front { top: 50px; background: var(--card-black); }
  .card--back { top: 511px; background: var(--card-black); }

  .silver-bar {
    position: absolute;
    width: 14px;
    border-radius: 7px;
    background: linear-gradient(90deg, var(--silver-dark), var(--silver-light) 45%, var(--silver-dark));
  }
  .card--front .silver-bar { top: 34px; height: 332px; }
  .card--front .silver-bar--left { left: 18px; }
  .card--front .silver-bar--right { right: 18px; }

  .front-mark {
    position: absolute;
    inset: 0;
    display: flex;
    flex-direction: column;
    align-items: center;
    justify-content: center;
    gap: 18px;
  }
  .wordmark-row { display: flex; align-items: center; gap: 22px; }
  .mark-square {
    width: 70px; height: 70px;
    border: 6px solid var(--gold);
  }
  .wordmark {
    font-size: 84px;
    font-weight: 700;
    letter-spacing: 2px;
    line-height: 1;
  }
  .card--front .wordmark { color: var(--text-light); }
  .tagline { font-size: 26px; letter-spacing: 1px; color: var(--text-light); }

  .contact-list {
    position: absolute;
    left: 48px;
    top: 62px;
    list-style: none;
    display: flex;
    flex-direction: column;
    gap: 30px;
  }
  .contact-item {
    display: flex;
    align-items: flex-start;
    gap: 20px;
    color: var(--text-light);
    font-size: 26px;
    line-height: 1.2;
  }
  .contact-icon {
    flex: none;
    width: 30px; height: 30px;
    background: var(--text-light);
    display: flex; align-items: center; justify-content: center;
    margin-top: 1px;
  }
  .contact-icon svg { width: 20px; height: 20px; }

  .identity-panel {
    position: absolute;
    top: 0; right: 0;
    width: 300px; height: 400px;
    background: var(--card-white);
    display: flex;
    flex-direction: column;
    align-items: center;
    justify-content: center;
    gap: 16px;
  }
  .card--back .silver-bar { left: -7px; top: 34px; height: 332px; }
  .identity-panel .mark-square { width: 52px; height: 52px; border: 0; background: var(--text-dark); }
  .identity-panel .wordmark { font-size: 60px; color: var(--maroon); }
  .identity-panel .wordmark-row { gap: 16px; }
  .identity-panel .tagline { font-size: 20px; color: var(--text-dark); }
</style>
</head>
<body>

<section class="card card--front" aria-label="Card front">
  <span class="silver-bar silver-bar--left"></span>
  <span class="silver-bar silver-bar--right"></span>
  <div class="front-mark">
    <div class="wordmark-row">
      <span class="mark-square"></span>
      <span class="wordmark">MB&amp;LR</span>
    </div>
    <p class="tagline">Bolt &amp; Lathe Rigging Co</p>
  </div>
</section>

<section class="card card--back" aria-label="Card back">
  <ul class="contact-list">
    <li class="contact-item">
      <span class="contact-icon">
        <svg viewBox="0 0 20 20"><rect x="6" y="2" width="8" height="16" rx="1.5" fill="none" stroke="#121212" stroke-width="2"/></svg>
      </span>
      <span>555.014.2290</span>
    </li>
    <li class="contact-item">
      <span class="contact-icon">
        <svg viewBox="0 0 20 20" fill="none" stroke="#121212" stroke-width="1.6"><circle cx="10" cy="10" r="8"/><ellipse cx="10" cy="10" rx="3.5" ry="8"/><line x1="2" y1="10" x2="18" y2="10"/></svg>
      </span>
      <span>www.mbandlr.com</span>
    </li>
    <li class="contact-item">
      <span class="contact-icon">
        <svg viewBox="0 0 20 20" fill="none" stroke="#121212" stroke-width="1.8"><rect x="2" y="4" width="16" height="12"/><polyline points="2,4 10,11 18,4"/></svg>
      </span>
      <span>sales@mbandlr.com</span>
    </li>
    <li class="contact-item">
      <span class="contact-icon">
        <svg viewBox="0 0 20 20"><path d="M10 1a6 6 0 0 0-6 6c0 4.5 6 12 6 12s6-7.5 6-12a6 6 0 0 0-6-6z" fill="#121212"/><circle cx="10" cy="7" r="2.2" fill="#e4e4e4"/></svg>
      </span>
      <span>48 Harbor Row<br>Millbrook-00410</span>
    </li>
  </ul>

  <div class="identity-panel">
    <span class="silver-bar"></span>
    <div class="wordmark-row">
      <span class="mark-square"></span>
      <span class="wordmark">MB&amp;LR</span>
    </div>
    <p class="tagline">Bolt &amp; Lathe Rigging Co</p>
  </div>
</section>

</body>
</html>
```